**** Business card design for VoltaNode ****

For my ICT company VoltaNode I need I need a business card design.

We design, build and host web-applications and we have our own CMS product.

Some good examples are attached.

The information should be:
Joris Tielenburg
Managing director
E: j.tielenburg@voltanode-example.nl
M: +31(0)6 57218064
T: +31(0)40 7249305
W: www.voltanode-example.nl

Address:
Berend Vlootweg 27
5612 KT Eindhoven

Industry/Entity Type

Business

Requirements
Must have
• - Use logo (see attachments)
- Double sided
- Distinctive
Nice to have
• - Place for a statement on the back-side: "Designed with knowledge, built with passion"
- HTML code (or Wordpress)
- Dark (black or dark-gray) side
- Small simple images for telephone, e-mail en Url.
- QR code (only if not disturbing), not required, just an option

```html
<!DOCTYPE html>
<html lang="en">
<head>
<meta charset="utf-8">
<title>VoltaNode business card</title>
<link rel="stylesheet" href="https://fonts.googleapis.com/css2?family=Open+Sans:wght@400;600&family=Arimo:wght@700&display=swap">
<style>
  :root {
    --backdrop: #e4e1dc;
    --card: #000000;
    --ink: #ffffff;
    --accent: #5fe3f2;
    --accent-deep: #1fa6e6;
    --brand-grey: #8fa3ad;
    --title-blue: #3cc6f0;
  }
  * { box-sizing: border-box; margin: 0; padding: 0; }
  html, body {
    width: 1200px; height: 1000px; overflow: hidden;
    background: var(--backdrop);
    font-family: "Open Sans", Arial, sans-serif;
  }
  .stage { position: relative; width: 1200px; height: 1000px; }
  .card {
    position: absolute; width: 751px; height: 444px;
    background: var(--card); color: var(--ink);
    box-shadow: 0 6px 18px rgba(0,0,0,0.25);
  }
  .card--front { left: 53px; top: 36px; }
  .card--back { left: 393px; top: 508px; }

  .brand { position: absolute; display: flex; align-items: center; }
  .brand__dot { border-radius: 50%; background: var(--accent-deep); flex: none; }
  .brand__name { color: var(--brand-grey); font-weight: 400; line-height: 1; letter-spacing: 0.5px; }

  .card--front .brand { left: 150px; top: 132px; gap: 30px; }
  .card--front .brand__dot { width: 118px; height: 118px; }
  .card--front .brand__name { font-size: 58px; }

  .tagline {
    position: absolute; left: 0; right: 0; top: 334px;
    text-align: center; color: var(--accent); font-size: 27px;
  }
  .front-url {
    position: absolute; left: 0; right: 0; top: 401px;
    text-align: center; color: var(--accent); font-size: 17px;
  }

  .card--back .brand { left: 370px; top: 64px; gap: 22px; }
  .card--back .brand__dot { width: 90px; height: 90px; }
  .card--back .brand__name { font-size: 46px; }

  .address { position: absolute; left: 56px; top: 152px; font-size: 17px; line-height: 23px; }

  .contact { position: absolute; left: 48px; list-style: none; font-size: 17px; line-height: 24px; }
  .contact--phones { top: 229px; }
  .contact--web { top: 309px; }
  .contact li { display: flex; align-items: center; gap: 6px; }
  .contact svg { width: 18px; height: 18px; flex: none; }

  .person { position: absolute; right: 52px; top: 250px; text-align: right; }
  .person__name { font-family: "Arimo", Arial, sans-serif; font-weight: 700; font-size: 32px; line-height: 36px; }
  .person__role { color: var(--title-blue); font-size: 20px; line-height: 22px; }
</style>
</head>
<body>
<main class="stage">
  <section class="card card--front" aria-label="Card front">
    <div class="brand">
      <span class="brand__dot"></span>
      <span class="brand__name">VoltaNode</span>
    </div>
    <p class="tagline">Designed with knowledge, built with passion</p>
    <p class="front-url">www.voltanode-example.nl</p>
  </section>

  <section class="card card--back" aria-label="Card back">
    <div class="brand">
      <span class="brand__dot"></span>
      <span class="brand__name">VoltaNode</span>
    </div>

    <p class="address">Berend Vlootweg 27<br>5612 KT Eindhoven</p>

    <ul class="contact contact--phones">
      <li>
        <svg viewBox="0 0 18 18" aria-hidden="true"><path d="M4 2.5l2.5 0 1.2 3-1.6 1.2c.8 1.8 2.2 3.2 4 4l1.2-1.6 3 1.2 0 2.5c0 .8-.7 1.4-1.5 1.3C7.4 13.5 4.5 10.6 3.9 4c-.1-.8.5-1.5 1.1-1.5z" fill="#fff"/><path d="M11 2.5a4.5 4.5 0 0 1 4.5 4.5M11 5a2 2 0 0 1 2 2" stroke="#fff" stroke-width="1.3" fill="none"/></svg>
        +31(0)40 7249305
      </li>
      <li>
        <svg viewBox="0 0 18 18" aria-hidden="true"><rect x="5" y="2" width="8" height="14" rx="1.5" fill="#fff"/><rect x="6.5" y="4" width="5" height="6" fill="#000"/><circle cx="9" cy="13" r="1" fill="#000"/></svg>
        +31(0)6 57218064
      </li>
    </ul>

    <ul class="contact contact--web">
      <li>
        <svg viewBox="0 0 18 18" aria-hidden="true"><rect x="2" y="4" width="14" height="10" rx="1" fill="#fff"/><path d="M2.5 4.5L9 10l6.5-5.5" stroke="#000" stroke-width="1.3" fill="none"/></svg>
        j.tielenburg@voltanode-example.nl
      </li>
      <li>
        <svg viewBox="0 0 18 18" aria-hidden="true"><g stroke="#fff" stroke-width="1.3" fill="none"><circle cx="9" cy="9" r="6.5"/><ellipse cx="9" cy="9" rx="2.8" ry="6.5"/><path d="M2.5 9h13M3.5 5.8h11M3.5 12.2h11"/></g></svg>
        www.voltanode-example.nl
      </li>
    </ul>

    <div class="person">
      <p class="person__name">Joris Tielenburg</p>
      <p class="person__role">Managing director</p>
    </div>
  </section>
</main>
</body>
</html>
```